DWR Logistics Marketing flyer

Good morning, I run a trucking company and I will be needing help setting up a website logo and a marketing flyer or something like that talking about our services and what we can offer to potential new customers who need to ship their product. I need help getting this all together.

Target Market(s)

Transportation customers

Requirements
Must have
• should list our services and contact info
Nice to have
• the Logo on the top

```html
<!DOCTYPE html>
<html lang="en">
<head>
<meta charset="utf-8">
<title>DWR Logistics – Marketing Flyer</title>
<link href="https://fonts.googleapis.com/css2?family=Mulish:wght@400;600;700&family=Oswald:wght@500;600&display=swap" rel="stylesheet">
<style>
  :root{
    --brand-blue:#0b0b93;
    --stage-grey:#97989c;
    --paper:#ffffff;
    --ink:#1d1d1d;
    --footer-black:#121212;
    --rule-grey:#c9c9cf;
  }
  *{margin:0;padding:0;box-sizing:border-box}
  html,body{width:1200px;height:1130px;overflow:hidden}
  body{background:var(--stage-grey);position:relative;font-family:"Mulish",sans-serif;color:var(--ink)}
  .abs{position:absolute}

  /* logo card */
  .logo-card{left:435px;top:47px;width:362px;height:252px;background:var(--paper);text-align:center}
  .logo-card .brand-name{position:absolute;left:0;right:0;top:120px;font-weight:700;font-size:24px;letter-spacing:1px;color:var(--brand-blue)}
  .logo-card .brand-est{position:absolute;left:0;right:0;top:166px;font-weight:700;font-size:12px;letter-spacing:.5px;color:var(--brand-blue)}
  .logo-card .brand-square{position:absolute;left:163px;top:72px;width:36px;height:36px;background:var(--brand-blue)}

  /* front page */
  .front{left:62px;top:397px;width:519px;height:671px;background:var(--paper)}
  .front .header-name{position:absolute;left:12px;top:38px;font-weight:700;font-size:11px;letter-spacing:.5px;color:var(--brand-blue)}
  .front .header-est{position:absolute;left:24px;top:55px;font-weight:600;font-size:8px;color:var(--brand-blue)}
  .contact{position:absolute;top:14px;padding-left:13px;border-left:3px solid var(--brand-blue);font-size:11px;line-height:16px}
  .contact .person{color:var(--brand-blue);font-weight:700}
  .contact .phone{font-weight:700}
  .hero-photo{position:absolute;left:0;top:74px;width:519px;height:176px;
    background:linear-gradient(100deg,#5b6f8a 0%,#e8a050 30%,#f2b860 45%,#c9604a 65%,#7c3b3e 85%,#43506a 100%)}
  .front .body-copy{position:absolute;left:18px;top:273px;width:479px;font-size:9.55px;line-height:13.25px;text-align:justify}
  .front .body-copy p{margin-bottom:13.25px}
  .front .bottom-band{position:absolute;left:0;bottom:0;width:100%;height:13px;background:var(--brand-blue)}

  /* back page */
  .back{left:628px;top:400px;width:519px;height:671px;background:var(--paper);overflow:hidden}
  .offer{position:absolute;left:0;top:0;width:100%;height:236px;background:var(--brand-blue);color:#fff}
  .section-title{font-family:"Oswald",sans-serif;font-weight:600;font-size:20px;letter-spacing:.3px}
  .offer .section-title{position:absolute;left:32px;top:21px}
  .offer-photo{position:absolute;left:29px;top:64px;width:148px;height:148px;border-radius:50%;
    background:radial-gradient(circle at 45% 40%,#c8614a 0%,#9a5a5e 30%,#2f8ea0 60%,#1c6f82 100%)}
  .offer .body-copy{position:absolute;left:209px;top:29px;width:284px;font-size:9.6px;line-height:13.85px;text-align:justify}
  .services-title{position:absolute;left:15px;top:248px;color:var(--brand-blue)}
  .service{position:absolute;width:235px;height:101px;border:1px solid var(--rule-grey)}
  .service .icon{position:absolute;left:12px;top:18px;width:44px;height:44px}
  .service h3{position:absolute;left:69px;top:14px;font-family:"Oswald",sans-serif;font-weight:500;font-size:14.5px;letter-spacing:.2px}
  .service p{position:absolute;left:70px;top:38px;width:152px;font-size:10.6px;line-height:12.2px}
  .contact-bar{position:absolute;left:0;bottom:0;width:100%;height:51px;background:var(--footer-black);color:#fff;
    font-family:"Oswald",sans-serif;font-weight:500;font-size:16px}
  .contact-bar .slash{position:absolute;left:0;top:0}
  .contact-bar .item{position:absolute;top:13px;display:flex;align-items:center;gap:8px;white-space:nowrap}
  .contact-bar .item-email{right:28px}
</style>
</head>
<body>

  <section class="abs logo-card">
    <div class="brand-square"></div>
    <div class="brand-name">DWR LOGISTICS LLC</div>
    <div class="brand-est">ESTABLISHED IN 2010</div>
  </section>

  <article class="abs front">
    <div class="header-name">DWR LOGISTICS LLC</div>
    <div class="header-est">ESTABLISHED IN 2010</div>
    <div class="contact" style="left:242px">
      <div class="person">Mara Kellan</div><div>CEO</div><div class="phone">555-301-4420</div>
    </div>
    <div class="contact" style="left:380px">
      <div class="person">Owen Tallis</div><div>CFO</div><div class="phone">555-301-7762</div>
    </div>
    <div class="hero-photo" role="img" aria-label="Photo of two workers in hard hats looking over trucks and stacked shipping containers at sunset"></div>
    <div class="body-copy">
      <p>We are a transportation company that specializes in logistics to maximize efficiency in getting the product from shipper to customer in the shortest safest time possible. We have the knowledge and ability to handle any dry van, Reefer, flatbed, or tanker load that needs to be moved, and strive to be your number one call to bring or move any product that your company may need. With our current 30 truck fleet We can service customers locally to across country with solo and team drivers to make sure that your product is to your customers in the time frame promised. We also can adjust to each customers needs so If the need arises, we can add to the fleet to make sure that you the customer are getting the service that you need. We take pride in our work and our customer service from pick up to delivery. Our current customer list handles more than half of the nation's orange Juice, hauling the corn oil that fries the potatoes chips for the one of the nations largest potato chip suppliers, to hauling wine from the west coast doing plant to plant transfers to the plants on the east coast. We also branch out to haul the corn syrup in to make the wine and alcohol out of the plant in the Midwest to the different plants that make alcohol. In short, from a transportation standpoint if you need it, we can bring it to you rather it is the ingredient's coming in to your plant or your product leaving.</p>
      <p>To date we have won the RLX carrier excellence award two years in a row servicing their major customers across the different brokerage networks along with we are the number one truck supplier to two of the major orange juice manufacturers in the US for when they bring their product into port side in Florida, and it needs to go to their manufacturing facility throughout the state. In the past year we have hauled over 40 million gallons of orange juice, another million gallons of wine and alcohol and millions of gallons of corn oil to service the nation's food industry with the ability to add to that ever-growing number. What sets us apart from any other carrier is that when you call you will get either the owner or the individual that makes as many decisions as possible, you will not have to wait for approvals and time wasted. We work through the problems to find the right solution then get it executed quickly and effectively. You are not just another number to us you are what make our company possible, and we value that relationship.</p>
      <p>Our references include those from</p>
      <p>Verano citrus products, Solfina North America, Crisply Snacks, and Ardent Spirits.</p>
    </div>
    <div class="bottom-band"></div>
  </article>

  <article class="abs back">
    <section class="offer">
      <h2 class="section-title">WHAT WE CAN OFFER</h2>
      <div class="offer-photo" role="img" aria-label="Aerial photo of a container ship loaded with colourful containers at sea"></div>
      <p class="body-copy">Sed ut perspiciatis unde omnis iste natus error sit voluptatem accusantium doloremque laudantium, totam rem aperiam, eaque ipsa quae ab illo inventore veritatis et quasi architecto beatae vitae dicta sunt explicabo. Nemo enim ipsam voluptatem quia voluptas sit aspernatur aut odit aut fugit, sed quia consequuntur magni dolores eos qui ratione voluptatem sequi nesciunt. Neque porro quisquam est, qui dolorem ipsum quia dolor sit amet, consectetur, adipisci velit, sed quia non numquam eius modi tempora incidunt ut labore et dolore magnam aliquam quaerat voluptatem. Ut enim ad minima veniam, quis nostrum exercitationem ullam corporis suscipit laboriosam, nisi ut aliquid ex ea commodi consequatur? Quis autem vel eum iure reprehenderit qui in ea voluptate velit esse quam nihil molestiae consequatur, vel illum qui dolorem eu.</p>
    </section>

    <h2 class="section-title services-title">OUR SERVICES</h2>

    <div class="service" style="left:17px;top:284px">
      <svg class="icon" viewBox="0 0 44 44"><circle cx="22" cy="22" r="22" fill="#0b0b93"/><path d="M19 11h6v4h4v5l4 2-3 8H14l-3-8 4-2v-5h4z" fill="#fff"/><path d="M11 32q3 2 5.5 0t5.5 0 5.5 0 5.5 0" stroke="#fff" stroke-width="2" fill="none"/></svg>
      <h3>LOREM IPSUM</h3>
      <p>Sed ut perspiciatis unde omnis iste natus error sit voluptatem accus antium doloremque lauda ntium, totam rem.</p>
    </div>
    <div class="service" style="left:262px;top:284px">
      <svg class="icon" viewBox="0 0 44 44"><circle cx="22" cy="22" r="22" fill="#0b0b93"/><path d="M10 15h17v13H10zM27 19h5l4 5v4h-9z" fill="#fff"/><circle cx="15" cy="29" r="3" fill="#fff" stroke="#0b0b93" stroke-width="1.5"/><circle cx="31" cy="29" r="3" fill="#fff" stroke="#0b0b93" stroke-width="1.5"/></svg>
      <h3>LOREM IPSUM</h3>
      <p>Sed ut perspiciatis unde omnis iste natus error sit voluptatem accus antium doloremque lauda ntium, totam rem.</p>
    </div>
    <div class="service" style="left:17px;top:395px">
      <svg class="icon" viewBox="0 0 44 44"><circle cx="22" cy="22" r="22" fill="#0b0b93"/><path d="M31 10q4-1 3 3l-5 5 3 12-2 2-5-9-5 5 1 4-2 2-2-5-5-2 2-2 4 1 5-5-9-5 2-2 12 3z" fill="#fff"/></svg>
      <h3>LOREM IPSUM</h3>
      <p>Sed ut perspiciatis unde omnis iste natus error sit voluptatem accus antium doloremque lauda ntium, totam rem.</p>
    </div>
    <div class="service" style="left:262px;top:395px">
      <svg class="icon" viewBox="0 0 44 44"><circle cx="22" cy="22" r="22" fill="#0b0b93"/><rect x="13" y="11" width="18" height="20" rx="4" fill="#fff"/><rect x="16" y="15" width="5" height="6" fill="#0b0b93"/><rect x="23" y="15" width="5" height="6" fill="#0b0b93"/><circle cx="17.5" cy="26" r="1.6" fill="#0b0b93"/><circle cx="26.5" cy="26" r="1.6" fill="#0b0b93"/><path d="M15 31l-3 4M29 31l3 4" stroke="#fff" stroke-width="2"/></svg>
      <h3>LOREM IPSUM</h3>
      <p>Sed ut perspiciatis unde omnis iste natus error sit voluptatem accus antium doloremque lauda ntium, totam rem.</p>
    </div>
    <div class="service" style="left:17px;top:506px">
      <svg class="icon" viewBox="0 0 44 44"><circle cx="22" cy="22" r="22" fill="#0b0b93"/><circle cx="19" cy="16" r="5" fill="#fff"/><path d="M10 32q0-9 9-9 4 0 6 2v7z" fill="#fff"/><circle cx="29" cy="29" r="4" fill="#fff"/><circle cx="29" cy="29" r="1.5" fill="#0b0b93"/></svg>
      <h3>LOREM IPSUM</h3>
      <p>Sed ut perspiciatis unde omnis iste natus error sit voluptatem accus antium doloremque lauda ntium, totam rem.</p>
    </div>
    <div class="service" style="left:262px;top:506px">
      <svg class="icon" viewBox="0 0 44 44"><circle cx="22" cy="22" r="22" fill="#0b0b93"/><path d="M24 14h-10v17h17v-10" stroke="#fff" stroke-width="2.5" fill="none"/><path d="M29 11l4 4-10 10h-4v-4z" fill="#fff"/></svg>
      <h3>LOREM IPSUM</h3>
      <p>Sed ut perspiciatis unde omnis iste natus error sit voluptatem accus antium doloremque lauda ntium, totam rem.</p>
    </div>

    <footer class="contact-bar">
      <svg class="slash" width="519" height="51" viewBox="0 0 519 51"><path d="M270 0h6l9 51h-6z" fill="#fff"/></svg>
      <div class="item" style="left:20px">
        <svg width="12" height="16" viewBox="0 0 12 16"><path d="M6 0a6 6 0 0 1 6 6c0 4-6 10-6 10S0 10 0 6a6 6 0 0 1 6-6z" fill="#fff"/><circle cx="6" cy="6" r="2.2" fill="#121212"/></svg>
        <span>140 Alder Ct. Brookvale, IN. 47000</span>
      </div>
      <div class="item item-email">
        <svg width="16" height="12" viewBox="0 0 16 12"><rect x=".75" y=".75" width="14.5" height="10.5" fill="none" stroke="#fff" stroke-width="1.5"/><path d="M1 1l7 6 7-6M1 11l5-5M15 11l-5-5" stroke="#fff" stroke-width="1.3" fill="none"/></svg>
        <span>dwrlogistics@mail.com</span>
      </div>
    </footer>
  </article>

</body>
</html>
```